Flyer design

We need a new flyer designed. We are not happy with our current design. We want to keep the pictures and basic info, just new design.

Target Market(s)

primarily multi family and HOA,s

Industry/Entity Type

Construction Company

Requirements
Must have
• Must have photos uploaded and use the text on the previous flyer. (also uploaded)

```html
<!DOCTYPE html>
<html lang="en">
<head>
<meta charset="utf-8">
<title>Stonecrest Construction Services – Flyer</title>
<link rel="stylesheet" href="https://fonts.googleapis.com/css2?family=Ubuntu:wght@300;400;500;700&family=Open+Sans:wght@400;600;700&display=swap">
<style>
  :root{
    --brand-blue:#3f63b4;
    --brand-blue-dark:#2f4f9c;
    --accent-blue:#5b87d6;
    --lavender:#c9cff0;
    --ink:#1e1e24;
    --muted:#6b6f7a;
    --paper:#ffffff;
    --stage:#eef0f4;
  }
  *{box-sizing:border-box;margin:0;padding:0}
  html,body{width:680px;height:1200px;overflow:hidden;background:var(--stage)}
  body{font-family:"Open Sans",sans-serif;color:var(--ink);position:relative}
  .flyer{position:absolute;left:20px;top:185px;width:640px;height:829px;background:var(--paper);overflow:hidden;box-shadow:0 10px 30px rgba(20,30,60,.25)}
  .flyer-art{position:absolute;left:0;top:0;width:640px;height:829px}
  .brand{position:absolute;left:32px;top:58px;display:flex;align-items:center;gap:12px}
  .brand-mark{width:44px;height:44px;background:var(--brand-blue)}
  .brand-name{font-family:"Ubuntu",sans-serif;font-weight:500;font-size:38px;line-height:1;color:var(--brand-blue)}
  .brand-sub{font-family:"Ubuntu",sans-serif;font-weight:400;font-size:14.5px;line-height:1;color:var(--brand-blue);margin-top:4px}
  .intro{position:absolute;left:36px;top:200px;width:290px}
  .intro-name{font-family:"Ubuntu",sans-serif;font-weight:500;font-size:18px;color:var(--brand-blue);line-height:1.1}
  .intro-sub{font-family:"Ubuntu",sans-serif;font-size:16px;color:var(--brand-blue);line-height:1.15}
  .intro-copy{font-size:11px;line-height:1.45;color:var(--ink)}
  .intro-copy b{font-weight:700}
  .intro-copy .caps{font-size:12.5px}
  .advantage-bar{position:absolute;left:0;top:332px;width:25px;height:163px;background:var(--brand-blue)}
  .advantage{position:absolute;left:38px;top:334px}
  .advantage-kicker{font-family:"Ubuntu",sans-serif;font-size:14px;line-height:1}
  .advantage-title{font-family:"Ubuntu",sans-serif;font-weight:300;font-size:34px;color:var(--brand-blue);line-height:1.05}
  .advantage-list{list-style:none;margin-top:6px}
  .advantage-list li{font-size:12px;line-height:18px;display:flex;align-items:center;gap:6px}
  .tick{width:13px;height:12px;flex:none}
  .sectors{position:absolute;left:44px;top:508px;font-family:"Ubuntu",sans-serif;font-weight:300;font-size:20px;line-height:25px;color:var(--accent-blue);text-transform:uppercase}
  .services-rule{position:absolute;left:342px;top:332px;width:2px;height:430px;background:var(--lavender)}
  .services{position:absolute;left:355px;top:338px}
  .services-title{font-family:"Ubuntu",sans-serif;font-size:26px;color:var(--brand-blue);line-height:1}
  .services-title small{font-size:13px;color:var(--ink)}
  .services-list{list-style:none;margin-top:8px}
  .services-list li{display:flex;align-items:center;gap:12px;height:29.2px;font-size:11.5px}
  .service-icon{width:25px;height:25px;flex:none}
  .footer{position:absolute;left:0;bottom:0;width:640px;height:124px;color:#fff;display:flex;align-items:flex-start;padding:22px 0 0 36px}
  .footer-col{font-family:"Ubuntu",sans-serif;font-size:12px;line-height:15px}
  .footer-col h3{font-weight:400;font-size:15px;line-height:18px}
  .footer-col.ca{width:160px}
  .footer-col.tx{width:140px;padding-left:16px;border-left:1px solid rgba(255,255,255,.5);height:64px}
  .footer-contact{padding-left:16px;border-left:1px solid rgba(255,255,255,.5);height:64px;font-family:"Ubuntu",sans-serif;padding-top:12px}
  .footer-contact .phone{font-size:19px;line-height:22px}
  .footer-contact .web{font-size:17px;line-height:22px}
</style>
</head>
<body>
<main class="flyer">
  <svg class="flyer-art" viewBox="0 0 640 829" aria-hidden="false">
    <defs>
      <linearGradient id="heroFade" x1="0" y1="0" x2="1" y2="0">
        <stop offset="0" stop-color="#ffffff" stop-opacity="0"/>
        <stop offset=".35" stop-color="#8fb0dd" stop-opacity=".7"/>
        <stop offset="1" stop-color="#4f78c4"/>
      </linearGradient>
      <linearGradient id="roofTone" x1="0" y1="0" x2="0" y2="1">
        <stop offset="0" stop-color="#7fa6dc" stop-opacity="0"/>
        <stop offset=".45" stop-color="#3c3b3e" stop-opacity=".85"/>
        <stop offset="1" stop-color="#2a2a2c" stop-opacity="0"/>
      </linearGradient>
      <linearGradient id="interiorTone" x1="0" y1="0" x2="1" y2="1">
        <stop offset="0" stop-color="#cfd9de"/><stop offset=".6" stop-color="#b88f6c"/><stop offset="1" stop-color="#7d5a45"/>
      </linearGradient>
      <linearGradient id="asphaltTone" x1="0" y1="0" x2="0" y2="1">
        <stop offset="0" stop-color="#8c9198"/><stop offset="1" stop-color="#3e4147"/>
      </linearGradient>
      <linearGradient id="facadeTone" x1="0" y1="0" x2="1" y2="1">
        <stop offset="0" stop-color="#d8cfc4"/><stop offset="1" stop-color="#8b8178"/>
      </linearGradient>
    </defs>
    <g role="img" aria-label="Photo of roofers replacing shingles on a pitched roof under a blue sky">
      <rect x="250" y="0" width="390" height="300" fill="url(#heroFade)"/>
      <path d="M380 300 L640 40 L640 300 Z" fill="url(#roofTone)"/>
    </g>
    <path d="M0 196 C120 160 250 176 330 214 C230 196 120 200 0 234 Z" fill="var(--lavender)" opacity=".7"/>
    <circle cx="258" cy="184" r="50" fill="#fff"/>
    <circle cx="258" cy="184" r="46" fill="url(#asphaltTone)" role="img" aria-label="Photo of workers laying fresh asphalt"/>
    <circle cx="396" cy="242" r="89" fill="#fff"/>
    <circle cx="396" cy="242" r="84" fill="url(#interiorTone)" role="img" aria-label="Photo of a renovated clubhouse lounge with sofas and large windows"/>
    <circle cx="559" cy="274" r="73" fill="#fff"/>
    <circle cx="559" cy="274" r="68" fill="url(#facadeTone)" role="img" aria-label="Photo of a lift working on a building facade"/>
    <path d="M0 668 C160 640 330 660 640 700 L640 829 L0 829 Z" fill="var(--lavender)"/>
    <path d="M0 676 C170 655 340 690 640 712 L640 829 L0 829 Z" fill="var(--brand-blue)"/>
  </svg>

  <header class="brand">
    <span class="brand-mark"></span>
    <div>
      <div class="brand-name">Stonecrest</div>
      <div class="brand-sub">Construction Services Inc.</div>
    </div>
  </header>

  <section class="intro">
    <h2 class="intro-name">Stonecrest</h2>
    <p class="intro-sub">Construction Services Inc.</p>
    <p class="intro-copy"><b>is your single source for all multi-family renovations.</b><br>
      Through the use of our client portal,<br>
      <b>we offer a high level of communication on<br>
      each project from <span class="caps">START TO FINISH.</span></b></p>
  </section>

  <div class="advantage-bar"></div>
  <section class="advantage">
    <p class="advantage-kicker">The Stonecrest</p>
    <h2 class="advantage-title">Advantage</h2>
    <ul class="advantage-list">
      <li><svg class="tick" viewBox="0 0 13 12"><path d="M1 6.5 L5 10.5 L12 1.5" fill="none" stroke="#4a4a52" stroke-width="2.4"/></svg>Hands on approach</li>
      <li><svg class="tick" viewBox="0 0 13 12"><path d="M1 6.5 L5 10.5 L12 1.5" fill="none" stroke="#4a4a52" stroke-width="2.4"/></svg>Level of communication with client</li>
      <li><svg class="tick" viewBox="0 0 13 12"><path d="M1 6.5 L5 10.5 L12 1.5" fill="none" stroke="#4a4a52" stroke-width="2.4"/></svg>Daily or weekly updates on every project</li>
      <li><svg class="tick" viewBox="0 0 13 12"><path d="M1 6.5 L5 10.5 L12 1.5" fill="none" stroke="#4a4a52" stroke-width="2.4"/></svg>Competitive pricing</li>
      <li><svg class="tick" viewBox="0 0 13 12"><path d="M1 6.5 L5 10.5 L12 1.5" fill="none" stroke="#4a4a52" stroke-width="2.4"/></svg>Due diligence</li>
      <li><svg class="tick" viewBox="0 0 13 12"><path d="M1 6.5 L5 10.5 L12 1.5" fill="none" stroke="#4a4a52" stroke-width="2.4"/></svg>Single source for all needs</li>
    </ul>
  </section>

  <p class="sectors">General contractor.<br>Multifamily.<br>Commercial.<br>Residential.<br>Due diligence.</p>

  <div class="services-rule"></div>
  <section class="services">
    <h2 class="services-title">Services <small>We Provide:</small></h2>
    <ul class="services-list">
      <li><svg class="service-icon" viewBox="0 0 25 25"><circle cx="12.5" cy="12.5" r="12" fill="var(--brand-blue)"/><path d="M6 16 L10 11 L13 14 L19 8" fill="none" stroke="#fff" stroke-width="2"/></svg>Roof replacements</li>
      <li><svg class="service-icon" viewBox="0 0 25 25"><circle cx="12.5" cy="12.5" r="12" fill="var(--brand-blue)"/><path d="M6 17 L17 17 L12 9 Z" fill="#fff"/></svg>Concrete repairs</li>
      <li><svg class="service-icon" viewBox="0 0 25 25"><circle cx="12.5" cy="12.5" r="12" fill="var(--brand-blue)"/><ellipse cx="12.5" cy="11.5" rx="6.5" ry="4.5" fill="none" stroke="#fff" stroke-width="1.6"/></svg>Consulting services</li>
      <li><svg class="service-icon" viewBox="0 0 25 25"><circle cx="12.5" cy="12.5" r="12" fill="var(--brand-blue)"/><rect x="8" y="6.5" width="9" height="12" fill="none" stroke="#fff" stroke-width="1.6"/><path d="M10 10h5M10 13h5M10 16h5" stroke="#fff"/></svg>Budget proposals</li>
      <li><svg class="service-icon" viewBox="0 0 25 25"><circle cx="12.5" cy="12.5" r="12" fill="var(--brand-blue)"/><path d="M7 18 L17 8" stroke="#fff" stroke-width="3"/></svg>Exterior siding and carpentry</li>
      <li><svg class="service-icon" viewBox="0 0 25 25"><circle cx="12.5" cy="12.5" r="12" fill="var(--brand-blue)"/><rect x="8" y="8" width="9" height="5" fill="#fff"/><path d="M12.5 13v6" stroke="#fff" stroke-width="2"/></svg>Exterior/interior paint</li>
      <li><svg class="service-icon" viewBox="0 0 25 25"><circle cx="12.5" cy="12.5" r="12" fill="var(--brand-blue)"/><path d="M9 7v10h8" fill="none" stroke="#fff" stroke-width="2.4"/></svg>Office and clubhouse remodeling</li>
      <li><svg class="service-icon" viewBox="0 0 25 25"><circle cx="12.5" cy="12.5" r="12" fill="var(--brand-blue)"/><path d="M12.5 6 C16 10 17 12 17 14 A4.5 4.5 0 0 1 8 14 C8 12 9 10 12.5 6 Z" fill="#fff"/></svg>Fire and flood damage build back</li>
      <li><svg class="service-icon" viewBox="0 0 25 25"><circle cx="12.5" cy="12.5" r="12" fill="var(--brand-blue)"/><path d="M7 7 L18 18 M18 7 L7 18" stroke="#fff" stroke-width="2"/></svg>Large scale interior renovations</li>
      <li><svg class="service-icon" viewBox="0 0 25 25"><circle cx="12.5" cy="12.5" r="12" fill="var(--brand-blue)"/><circle cx="12.5" cy="14.5" r="3" fill="#fff"/><circle cx="8.5" cy="10" r="1.5" fill="#fff"/><circle cx="12.5" cy="8.5" r="1.5" fill="#fff"/><circle cx="16.5" cy="10" r="1.5" fill="#fff"/></svg>Dog parks</li>
      <li><svg class="service-icon" viewBox="0 0 25 25"><circle cx="12.5" cy="12.5" r="12" fill="var(--brand-blue)"/><path d="M6 17 L19 9" stroke="#fff" stroke-width="3"/></svg>Asphalt paving</li>
    </ul>
  </section>

  <footer class="footer">
    <address class="footer-col ca" style="font-style:normal">
      <h3>California Address :</h3>
      1280 Meridian Ave.<br>Suite 300 Lakeview,<br>CA. 90000
    </address>
    <address class="footer-col tx" style="font-style:normal">
      <h3>Texas Address :</h3>
      3540 Cedar Ridge Rd.<br>Suite 210-118<br>Oakdale TX. 75000
    </address>
    <div class="footer-contact">
      <div class="phone">(555) 014-2287</div>
      <div class="web">www.stonecrestbuilders.com</div>
    </div>
  </footer>
</main>
</body>
</html>
```